Fresh and Modern Real Estate Land Website

This Real Estate Agent sells only land.
The wordpress design will need to work well with responsive Avada theme.
Colors should complement the attached Home-Header.jpg, the Sonoran Desert, Southwest Region of Arizona and Tucson.
Home page layout to include
- Logo Attached: NewLogo.png
- Agent Photo: MaeDorn.jpg
- Contact Detials: use Phone
- Slogan: "I've Never Shown a House"
- Static header or Main image (see Attached Home-Header.jpg) - The dimensions of this shot may not be correct for your design. Please select from similar stock if needed and provide stock photo id.
- Intro/Welcome Text See Attached: Intro.txt
- Vertical or Horizontal display of "New" listings (include: Photo, Price, exerpt/intro) see: Properties.zip
- Tools of the trade. Home page will have a section called "Tools Of the Trade" These are items the agent uses in her work. This seciton will need to be 3 or More Images about 100 characters of text and Title. These will rotate through about 12 different tools. see: tools-of-the-trade.zip
Footer to include Contact Info/Recent Blog Posts/Testimonial
No Social Network icons
Main Menu:
Home
Properties
Testimonials
Services
About Mae
Blog
Contact
- Marck Script google/Times new Roman is logo. Designers Choice.

```html
<!DOCTYPE html>
<html lang="en">
<head>
<meta charset="utf-8">
<title>Mae Dorn – Land Website Home</title>
<link href="https://fonts.googleapis.com/css2?family=Open+Sans:wght@400;600;700&display=swap" rel="stylesheet">
<style>
  :root {
    --page-bg: #ffffff;
    --orange: #f37b21;
    --orange-dark: #e06a12;
    --blue: #1f64a8;
    --navy: #244d78;
    --text: #333333;
    --muted: #7a7a7a;
    --line: #dcdcdc;
    --overlay: rgba(20, 20, 20, 0.82);
    --sky-top: #2f7fd0;
    --sky-low: #9fc8ea;
    --rock: #b78261;
    --scrub: #4f6a35;
    --sunset-top: #6a3a1c;
    --sunset-mid: #f0a02a;
    --sunset-low: #2b1a10;
  }
  * { box-sizing: border-box; margin: 0; padding: 0; }
  html, body { width: 1200px; height: 686px; overflow: hidden; background: var(--page-bg); }
  body { font-family: "Open Sans", Arial, sans-serif; color: var(--text); }
  .canvas { position: relative; width: 1200px; height: 686px; overflow: hidden; }
  .site { position: absolute; left: 160px; top: 0; width: 880px; height: 686px; }

  .site-header { position: absolute; top: 12px; left: 0; width: 880px; height: 52px; }
  .brand { position: absolute; left: 0; top: 8px; display: flex; align-items: center; gap: 8px; }
  .brand-mark { width: 14px; height: 14px; border-radius: 50%; background: var(--orange); }
  .brand-name { font-size: 26px; font-weight: 700; color: var(--orange); line-height: 1; }
  .lang { position: absolute; right: 0; top: 0; font-size: 10px; color: var(--muted); display: flex; align-items: center; gap: 4px; }
  .lang-flag { width: 11px; height: 8px; background: var(--navy); }
  .search { position: absolute; right: 0; top: 22px; width: 120px; height: 20px; border: 1px solid var(--line); border-radius: 3px; font-size: 9px; color: var(--muted); padding: 3px 6px; }
  .search svg { position: absolute; right: 5px; top: 4px; }

  .main-nav { position: absolute; top: 70px; left: 0; width: 880px; height: 28px; background: var(--orange); border-radius: 2px; display: flex; justify-content: flex-end; align-items: center; padding-right: 60px; gap: 20px; }
  .main-nav a { color: #fff; font-size: 12px; font-weight: 600; text-decoration: none; }

  .hero { position: absolute; top: 106px; left: 0; width: 880px; height: 226px; overflow: hidden; }
  .hero-photo { position: absolute; inset: 0; background: linear-gradient(180deg, var(--sky-top) 0%, var(--sky-low) 48%, var(--rock) 62%, var(--scrub) 82%, #3c4f29 100%); }
  .hero-caption { position: absolute; left: 0; top: 48px; width: 222px; height: 124px; background: var(--overlay); color: #fff; padding: 10px 12px; }
  .hero-caption h2 { font-size: 14px; font-weight: 600; margin-bottom: 6px; }
  .hero-caption p { font-size: 10px; line-height: 1.35; }
  .btn { display: inline-block; background: var(--orange); color: #fff; font-size: 10px; font-weight: 600; border-radius: 2px; }
  .hero-caption .btn { margin-top: 8px; padding: 4px 8px; font-size: 11px; }
  .slider-dots { position: absolute; left: 10px; top: 184px; display: flex; gap: 4px; }
  .slider-dots span { width: 8px; height: 5px; background: #bbb; }
  .slider-dots span.active { background: #fff; }
  .hero-next { position: absolute; right: 8px; top: 98px; }

  .listings { position: absolute; top: 346px; left: 0; width: 880px; display: flex; gap: 20px; }
  .listing { width: 280px; }
  .listing-photo { position: relative; height: 100px; }
  .listing-photo.scrub { background: linear-gradient(180deg, #8db6d8 0%, #bcd2e2 35%, #6f8a4c 60%, #48602f 100%); }
  .listing-photo.sunset { background: linear-gradient(180deg, var(--sunset-top) 0%, var(--sunset-mid) 50%, #d9641c 68%, var(--sunset-low) 100%); }
  .listing-photo.ridge { background: linear-gradient(180deg, #9ec3e4 0%, #c9d9e6 38%, #8e8a6a 58%, #5c6a3c 100%); }
  .listing-photo svg { position: absolute; left: 0; top: 0; }
  .listing-meta { display: flex; justify-content: space-between; font-size: 11px; font-weight: 600; color: var(--blue); margin-top: 5px; }
  .listing-foot { position: relative; margin-top: 6px; height: 2px; background: var(--orange); }
  .listing-foot .btn { position: absolute; left: 50%; top: -7px; transform: translateX(-50%); padding: 1px 10px; font-size: 9px; }

  .intro { position: absolute; top: 486px; left: 120px; width: 640px; text-align: center; }
  .intro h3 { font-size: 12px; color: var(--orange); font-weight: 600; margin-bottom: 4px; }
  .intro p { font-size: 10px; color: var(--muted); line-height: 1.4; }

  .footer-boxes { position: absolute; top: 562px; left: 0; width: 880px; display: flex; gap: 20px; }
  .box { border: 1px solid var(--line); height: 112px; }
  .box-head { height: 20px; background: var(--blue); color: #fff; font-size: 10px; font-weight: 600; padding: 3px 8px; display: flex; justify-content: space-between; align-items: center; }
  .box-arrows { display: flex; gap: 3px; }
  .box-arrows span { width: 12px; height: 12px; background: #fff; display: flex; align-items: center; justify-content: center; }
  .about-box { width: 290px; }
  .about-body { display: flex; gap: 10px; padding: 10px; font-size: 10px; line-height: 1.4; color: var(--muted); }
  .agent-photo { width: 54px; height: 68px; flex: none; background: linear-gradient(180deg, #c9a58a, #8a6a58); }
  .about-body .phone { color: var(--blue); font-weight: 600; display: block; margin-top: 6px; }
  .tools-box { width: 570px; }
  .tools-row { display: flex; justify-content: space-around; padding: 10px 10px 0; }
  .tool { width: 110px; text-align: center; font-size: 10px; color: var(--text); }
  .tool-image { width: 48px; height: 40px; margin: 0 auto 4px; border-radius: 4px; }
  .tool-image.gps { background: #e3b512; }
  .tool-image.boots { background: #2c2c2c; }
  .tool-image.optics { background: #3a3a3a; }
  .tool-image.map { background: #d23a2a; }
  .tool .btn { margin-top: 4px; padding: 1px 10px; font-size: 9px; }
</style>
</head>
<body>
<div class="canvas">
  <div class="site">
    <header class="site-header">
      <div class="brand">
        <span class="brand-mark"></span>
        <span class="brand-name">Mae Dorn</span>
      </div>
      <div class="lang">ENG <span class="lang-flag"></span></div>
      <div class="search">Search site
        <svg width="10" height="10" viewBox="0 0 10 10"><circle cx="4" cy="4" r="3" fill="none" stroke="#1f64a8" stroke-width="1.4"/><line x1="6.2" y1="6.2" x2="9.5" y2="9.5" stroke="#1f64a8" stroke-width="1.4"/></svg>
      </div>
    </header>

    <nav class="main-nav">
      <a href="#">Home</a><a href="#">Properties</a><a href="#">Testimonials</a><a href="#">Services</a><a href="#">About Mae</a><a href="#">Blog</a><a href="#">Contact</a>
    </nav>

    <section class="hero">
      <div class="hero-photo" role="img" aria-label="Sonoran Desert landscape with saguaro cacti and red rock mountains under blue sky"></div>
      <div class="hero-caption">
        <h2>"I've Never Shown a House"</h2>
        <p>Lorem ipsum dolor sit amet, conse ctetur adipisicing elit, sed do eiusm od tempor incididunt ut labore et dolore magna aliqua.</p>
        <span class="btn">Learn More</span>
      </div>
      <div class="slider-dots"><span class="active"></span><span></span><span></span><span></span></div>
      <svg class="hero-next" width="14" height="22" viewBox="0 0 14 22"><polyline points="2,2 12,11 2,20" fill="none" stroke="#fff" stroke-width="2"/></svg>
    </section>

    <section class="listings">
      <article class="listing">
        <div class="listing-photo scrub" role="img" aria-label="Desert land parcel with green scrub and distant hills">
          <svg width="34" height="34" viewBox="0 0 34 34"><polygon points="0,0 34,0 0,34" fill="#1a1a1a"/><circle cx="10" cy="10" r="5" fill="none" stroke="#fff" stroke-width="1.6"/></svg>
        </div>
        <div class="listing-meta"><span>Label here</span><span>$150,000</span></div>
        <div class="listing-foot"><span class="btn">Details</span></div>
      </article>
      <article class="listing">
        <div class="listing-photo sunset" role="img" aria-label="Orange desert sunset over dark mountain ridge">
          <svg width="34" height="34" viewBox="0 0 34 34"><polygon points="0,0 34,0 0,34" fill="#1a1a1a"/><circle cx="10" cy="10" r="5" fill="none" stroke="#fff" stroke-width="1.6"/></svg>
        </div>
        <div class="listing-meta"><span>Label here</span><span>$150,000</span></div>
        <div class="listing-foot"><span class="btn">Details</span></div>
      </article>
      <article class="listing">
        <div class="listing-photo ridge" role="img" aria-label="Open desert lot with cacti and mountain range">
          <svg width="34" height="34" viewBox="0 0 34 34"><polygon points="0,0 34,0 0,34" fill="#1a1a1a"/><circle cx="10" cy="10" r="5" fill="none" stroke="#fff" stroke-width="1.6"/></svg>
        </div>
        <div class="listing-meta"><span>Label here</span><span>$150,000</span></div>
        <div class="listing-foot"><span class="btn">Details</span></div>
      </article>
    </section>

    <section class="intro">
      <h3>Welcome to Tucson Land</h3>
      <p>Finding the right piece of desert land takes patience, local knowledge and a trusted guide. I help buyers and sellers across southern Arizona with raw land, ranch parcels and lots.</p>
      <p>Browse new listings below or call me to talk about your plans.</p>
    </section>

    <section class="footer-boxes">
      <div class="box about-box">
        <div class="box-head">About Mae</div>
        <div class="about-body">
          <div class="agent-photo" role="img" aria-label="Portrait photo of the agent"></div>
          <div>Mae has sold land in the Sonoran Desert for over twenty years.
            <span class="phone">Call (520) 555-0148</span>
          </div>
        </div>
      </div>
      <div class="box tools-box">
        <div class="box-head">Tools of the Trade
          <div class="box-arrows">
            <span><svg width="6" height="8" viewBox="0 0 6 8"><polyline points="5,0 1,4 5,8" fill="none" stroke="#1f64a8" stroke-width="1.5"/></svg></span>
            <span><svg width="6" height="8" viewBox="0 0 6 8"><polyline points="1,0 5,4 1,8" fill="none" stroke="#1f64a8" stroke-width="1.5"/></svg></span>
          </div>
        </div>
        <div class="tools-row">
          <div class="tool"><div class="tool-image gps" role="img" aria-label="Handheld GPS unit"></div>GPS Unit<br><span class="btn">More</span></div>
          <div class="tool"><div class="tool-image boots" role="img" aria-label="Pair of field boots"></div>Field Boots<br><span class="btn">More</span></div>
          <div class="tool"><div class="tool-image optics" role="img" aria-label="Binoculars"></div>Binoculars<br><span class="btn">More</span></div>
          <div class="tool"><div class="tool-image map" role="img" aria-label="Folded trail map"></div>Trail Map<br><span class="btn">More</span></div>
        </div>
      </div>
    </section>
  </div>
</div>
</body>
</html>
```